Simple Website for Psychic Reader
Your chance to ‘see’ MY future! Quiet Harbors
Project: Simple Website for Psychic Reader
Simple Website for Psychic Reader - Miscellaneous
Creative Brief
Miscellaneous
www.quietharborsx.com
Privately owned site for psychic reader that does private readings ( in person and telephone) I work at tradeshows, do private parties, charity events, newspaper and radio exposure. I do a very corporate job during the day, and follow my passion and gift of doing psychic readings part My goal is to expand my footprint via the web as most clients like to make contact prior to tradeshow events, as well would like to increase exposure via web by adding links to follow me on Chatterbox , Pipwing , Talkora At the present time I am the only reader, but would like to include other psychics in future; each with their own profile page with a picture and brief blurb about themselves There are no applications to link or registration type processes; I envision fairly standard pages such Home, Contact Us, Events, About Us, Blog or Links etc. . I’m not a religious person , but am spiritual. I’m a gentle soul as they say; fairly laid back, calm, straight forward and would like the website to reflect my personality as well as appearing professional and inviting versus a ‘circus sideshow’ Name of the company is Quiet Harbors. The company slogan is “Guiding you through your life path journey”
- figures that look like clip art or cartoons - nothing that casts an image of a psychic being a gypsy or witch - nothing too religious - more spiritual ; i.e. no crosses, no bibles etc - clutter - not fond of green as the main colour
Modern
Shades of purple; Royal purple, light purple, violet
Shades of blue –
Golden/Yellow – Open to almost all colours schemes
below header
http://www.qorvilwebx.ca
http://dervoshex.com/
http://brandlumpex.ca/
I enjoy flowing lines , ribbon swirls and a 3D look to webpages I’ll provide daily feedback and comments on each draft submitted Let me thank you in advance for taking the time and interest in sharing your creativity and for assisting me in my goals I look forward to working with you.
BriPepperel BriPepperel
We're getting down to the last couple days of the submission deadline. Please keep the draft submissions coming!!! I would like to any and all ideas you have for my wesite ! I will say the process has been a bit overwhelming for me .. and thanks for your patience in answering my 'stupid' questions Looking forward to your submissions .. Gwen
For those designers submitting drafts, I want to assure you I do provide prompt feedback to everyone for their designs, usually within a couple of hours of you submitting the drafts I highly value your time and effort and thank you again for all the designs submitted so far ... Keep the creative juices flowing!!!
Thank you for the drafts submitted so far - very much appreciated I'll provide some generic feedback as a composite of all drafts I've seen so far : 1) If the logo is going to be in a header box at the top, would prefer it's done in the original purple colour contained in the logo file 2) Like a 3D effect on the front page to give the overall look some depth 3) I generally prefer pictures without people in them 4) Content to include on the homepage would include areas for such things as Quotes, Overview, News bullets 5) Please include some area if not on the header that will contain the following : a) My Toll Free number , b) email, c)Place to put Tlakora Online indicator button 6) Keep the colours calm and cool - purples, blues, and try to incorporate some visual movement to the page - 3d, soft ribbon lines etc Great job so far ... Looking forward to seeing those creative minds at work
Please note the example of homepage uploaded - the content of it is no longer valid. I will be the only reader on the site - I don't require the boxes to show the online psychics or thumbnail table of the psychic profiles Homepage content will have items such as current news, my philosophy, links to call my toll free number or see upcoming events
Company Slogan is as follows: Guiding you through your life path journey
Dear Developers, I very much appreciate your dedicated work and thank you in advance for submitting designs. Feel free to colour outside of the lines and get creative ! I look forward to work with you all - thank you again for your all your efforts - Gwen
Sorry - in the design concept - I would like the menu bar below the header - NOT on left, my apologies for the error

```html
<!DOCTYPE html>
<html lang="en">
<head>
<meta charset="utf-8">
<title>Quiet Harbors – Psychic Readings</title>
<link rel="stylesheet" href="https://fonts.googleapis.com/css2?family=Arimo:wght@400;700&display=swap">
<style>
:root{
  --plum-deep:#2e0830;
  --plum:#5a1763;
  --plum-bright:#7a2a86;
  --violet-text:#7b2c86;
  --ink:#333;
  --muted:#666;
  --rule:#d8d8d8;
  --paper:#fff;
  --sky:#1b8fd8;
}
*{box-sizing:border-box;margin:0;padding:0}
html,body{width:1200px;height:1049px;overflow:hidden}
body{
  font-family:"Arimo",Arial,sans-serif;
  background:radial-gradient(ellipse at 50% 45%,#74246f 0%,#4b1250 45%,var(--plum-deep) 100%);
  position:relative;color:var(--ink);
}
.page{position:absolute;left:134px;top:51px;width:932px;height:940px;background:var(--paper);border-radius:6px;box-shadow:0 0 24px rgba(0,0,0,.45)}
.abs{position:absolute}

/* header */
.brand{left:150px;top:71px;width:228px;height:142px;background:linear-gradient(160deg,var(--plum-bright),var(--plum) 60%,#46104f);display:flex;align-items:center;justify-content:center;gap:10px;color:#fff;font-size:24px;font-weight:700}
.brand .dot{width:26px;height:26px;border-radius:50%;background:#fff}
.header-bar{left:378px;top:71px;width:680px;height:142px;background:linear-gradient(#fff,#f1f1f1);border-bottom:4px solid var(--plum)}
.online{left:700px;top:86px;width:170px;height:30px;border-radius:4px;background:linear-gradient(#4fb6f0,var(--sky));color:#fff;font-size:13px;display:flex;align-items:center;justify-content:center}
.online svg{position:absolute;left:-8px;top:-6px}
.email{left:660px;top:124px;font-size:15px;color:var(--ink);display:flex;align-items:center;gap:8px}
.tollfree{left:910px;top:71px;width:148px;height:71px;background:linear-gradient(var(--plum-bright),var(--plum));color:#fff;padding:14px 0 0 48px;font-size:15px;line-height:19px}
.tollfree svg{position:absolute;left:12px;top:10px}
.nav{left:390px;top:174px;width:660px;display:flex;justify-content:space-between;font-size:15px}
.nav a{color:var(--ink);text-decoration:none;padding:0 14px;border-right:1px solid #999;line-height:22px}
.nav a:last-child{border-right:0}

/* hero */
.hero{left:156px;top:233px;width:876px;height:415px;border-radius:4px;box-shadow:0 3px 10px rgba(0,0,0,.4);
  background:radial-gradient(ellipse at 55% 75%,rgba(255,196,90,.95) 0%,rgba(214,120,30,.7) 22%,rgba(90,40,10,.5) 45%,#050403 70%),#050403}
.hero-line{color:#fff;font-size:21px;letter-spacing:4px;text-transform:uppercase}

/* welcome */
.welcome{left:165px;top:694px;width:520px}
.welcome h1{font-size:28px;font-weight:400;color:var(--ink);margin-bottom:12px;line-height:34px}
.welcome h1 span{color:var(--violet-text)}
.welcome p{font-size:11.5px;line-height:15px;color:var(--muted);margin-bottom:10px}
.welcome a{color:var(--violet-text);font-weight:700;text-decoration:none}

/* events */
.events{left:705px;top:697px;width:327px;height:88px;background:#fff;box-shadow:0 1px 5px rgba(0,0,0,.25)}
.events h2{background:linear-gradient(var(--plum-bright),var(--plum));color:#fff;font-size:16px;font-weight:400;padding:8px 12px}
.events .entry{padding:5px 12px 0;font-size:10px;line-height:12px;color:var(--muted)}
.events .entry b{color:var(--ink)}
.events .all{position:absolute;right:10px;bottom:4px;font-size:10px;line-height:12px;color:var(--ink)}
.book{left:705px;top:793px;width:327px;height:34px;border-radius:8px;background:linear-gradient(#6e2478,#3e0b44);color:#fff;font-size:18px;display:flex;align-items:center;padding-left:14px;gap:12px;box-shadow:0 2px 5px rgba(0,0,0,.35);text-decoration:none}
.book .dot{width:15px;height:15px;border-radius:50%;background:#fff}
.click{left:900px;top:830px;width:122px;text-align:right;font-size:10px;line-height:12px;color:var(--ink)}

/* footer */
.footer-rule{left:150px;top:846px;width:900px;height:1px;background:var(--rule)}
.col-title{font-size:15px;color:var(--ink)}
.divider{width:1px;height:120px;background:var(--rule);top:853px}
.links{font-size:11.5px;line-height:24px;list-style:none;color:var(--ink)}
.links li::before{content:"";display:inline-block;width:6px;height:6px;background:var(--plum);margin-right:12px;vertical-align:middle}
.social{display:flex;gap:18px}
.social span{width:36px;height:36px;border-radius:50%;background:linear-gradient(#e6eef8,#b9cce3);box-shadow:0 1px 3px rgba(0,0,0,.3)}
.address{left:815px;top:890px;width:200px;padding-top:6px;border-top:1px solid var(--rule);font-size:12px;line-height:20px}
.copyright{left:0;top:1007px;width:1200px;text-align:center;color:#fff;font-size:11.5px}
</style>
</head>
<body>
<div class="page"></div>

<header>
  <div class="abs brand"><span class="dot"></span>Quiet Harbors</div>
  <div class="abs header-bar"></div>
  <div class="abs online">
    <svg width="34" height="34" viewBox="0 0 34 34"><circle cx="17" cy="17" r="15" fill="#4cb648" stroke="#fff" stroke-width="2"/><path d="M9 17l6 6 11-12" fill="none" stroke="#fff" stroke-width="4"/></svg>
    I'm online
  </div>
  <div class="abs email">
    <svg width="20" height="14" viewBox="0 0 20 14"><rect x="0.5" y="0.5" width="19" height="13" fill="#fff" stroke="#666"/><path d="M1 1l9 7 9-7" fill="none" stroke="#666"/></svg>
    info@quietharborsx.com
  </div>
  <div class="abs tollfree">
    <svg width="28" height="28" viewBox="0 0 28 28"><circle cx="14" cy="14" r="13" fill="#fff"/><path d="M8 11c0-2 2-3 6-3s6 1 6 3l-2 1-1-2h-6l-1 2zM9 14h10l1 6H8z" fill="#5a1763"/></svg>
    Toll Free:<br><b>800-555-0142</b>
  </div>
  <nav class="abs nav">
    <a href="#">Home</a><a href="#">Contact Us</a><a href="#">Events</a><a href="#">About Us</a><a href="#">Our Blog</a><a href="#">Testimonials</a>
  </nav>
</header>

<section class="abs hero" role="img" aria-label="Photograph of rows of lit tea-light candles glowing in the dark"></section>
<div class="abs hero-line" style="left:190px;top:258px">Guiding your through</div>
<div class="abs hero-line" style="left:330px;top:296px">your life path journey</div>

<main>
  <section class="abs welcome">
    <h1>Welcome to <span>Quiet harbors</span></h1>
    <p>Welcome to a calm space for insight and reflection. Private readings are offered in person and by telephone, at tradeshows, private parties and charity events. Each session is gentle, honest and straightforward, helping you find clarity on what matters most.</p>
    <p>Readings can be booked ahead of upcoming events or arranged privately. Call the toll free line or send an email to reserve your session. <a href="#">read more</a></p>
  </section>

  <aside class="abs events">
    <h2>Upcoming Events</h2>
    <div class="entry"><b>10 September, 2011</b><br>Join me at the Harbour Wellness Fair for private readings and a short talk on your path. <b>more...</b></div>
    <div class="all">...View all</div>
  </aside>
  <a class="abs book" href="#"><span class="dot"></span>Book a Reading</a>
  <div class="abs click">...Click here</div>
</main>

<footer>
  <div class="abs footer-rule"></div>
  <div class="abs col-title" style="left:165px;top:860px">More Info</div>
  <ul class="abs links" style="left:165px;top:888px"><li>Feedback</li><li>Overview</li><li>Online Registration</li></ul>
  <ul class="abs links" style="left:320px;top:888px"><li>Sitemap</li><li>The psychics</li><li>Online Advisors</li></ul>
  <div class="abs divider" style="left:510px"></div>
  <div class="abs col-title" style="left:530px;top:860px">Follow us</div>
  <div class="abs social" style="left:525px;top:905px"><span></span><span></span><span></span></div>
  <div class="abs divider" style="left:800px"></div>
  <div class="abs col-title" style="left:815px;top:860px">Contact Us</div>
  <div class="abs address">Address Line 1<br>Address line 2<br>Phone: 123 456 789</div>
  <div class="abs copyright">Copyright © 2011, Quiet Harbors All Rights Reserved.</div>
</footer>
</body>
</html>
```